Online-Marketing Material für Autohaus mit Werkstätten
Zielgruppe
Wir betreiben ein Autohaus mit Werkstätte und suchen hierfür Auszubildende in folgenden Berufen:
Kfz-Mechatroniker, Automobilkaufmann, Fachkraft für Lagerlogistik.
Aufgabenstellung
Die Post sollen Jugendliche ansprechen und sich an dem bisherigen Layout orientieren.

```html
<!DOCTYPE html>
<html lang="de">
<head>
<meta charset="utf-8">
<title>Ausbildung bei wagenfeld</title>
<link rel="stylesheet" href="https://fonts.googleapis.com/css2?family=Roboto:wght@400;500;700;900&display=swap">
<style>
  :root {
    --ink: #111111;
    --brand-navy: #1c2c6b;
    --brand-blue: #2a4fa8;
    --accent-yellow: #f2ee1f;
    --white: #ffffff;
  }
  html, body { margin: 0; padding: 0; overflow: hidden; }
  body { width: 1200px; height: 1200px; font-family: "Roboto", Arial, sans-serif; color: var(--ink); }
  .post { position: relative; width: 1200px; height: 1200px; overflow: hidden; background: var(--white); }

  .workshop-photo {
    position: absolute; inset: 0;
    background:
      radial-gradient(ellipse 300px 420px at 980px 560px, #2f5fc4 0%, rgba(47,95,196,0) 70%),
      linear-gradient(90deg, #e9edf2 0%, #cfd8e3 40%, #5a6a80 62%, #1e2a3e 78%, #24324c 100%);
  }
  .fade-left {
    position: absolute; inset: 0;
    background: linear-gradient(90deg, rgba(255,255,255,0.96) 0%, rgba(255,255,255,0.85) 35%, rgba(255,255,255,0.35) 58%, rgba(255,255,255,0) 72%);
  }
  .fade-bottom {
    position: absolute; left: 0; right: 0; bottom: 0; height: 220px;
    background: linear-gradient(180deg, rgba(255,255,255,0) 0%, rgba(255,255,255,0.75) 60%, rgba(255,255,255,0.85) 100%);
  }

  .brand { position: absolute; left: 110px; top: 120px; display: flex; align-items: center; gap: 14px; }
  .brand-mark { width: 26px; height: 26px; background: var(--brand-navy); }
  .brand-name { font-size: 44px; font-weight: 500; color: var(--brand-navy); letter-spacing: 0.5px; }

  .eyebrow { position: absolute; left: 114px; top: 336px; margin: 0; font-size: 24px; font-weight: 400; letter-spacing: 2.5px; }

  .headline { position: absolute; left: 108px; top: 398px; margin: 0; font-size: 91px; font-weight: 900; line-height: 89px; letter-spacing: 1px; text-transform: uppercase; }
  .slash { display: inline-block; width: 14px; height: 54px; background: var(--accent-yellow); transform: skewX(-20deg); margin-left: 30px; vertical-align: -2px; }

  .professions { position: absolute; left: 112px; top: 695px; margin: 0; padding: 0; list-style: none; font-size: 40px; font-weight: 400; line-height: 64px; }

  .apply-button { position: absolute; left: 112px; top: 913px; width: 538px; height: 84px; border-radius: 42px; background: var(--brand-navy); color: var(--white); display: flex; align-items: center; justify-content: center; font-size: 27px; font-weight: 700; letter-spacing: 1px; text-decoration: none; }

  .contact { position: absolute; top: 1092px; display: flex; align-items: center; gap: 21px; font-size: 24px; }
  .contact--web { left: 111px; }
  .contact--mail { left: 591px; }
  .contact-icon { width: 52px; height: 52px; border-radius: 50%; background: var(--brand-navy); display: flex; align-items: center; justify-content: center; }
  .chevrons { position: absolute; left: 1024px; top: 1100px; }
</style>
</head>
<body>
<main class="post">
  <div class="workshop-photo" role="img" aria-label="Foto: lächelnder Auszubildender in blauer Arbeitskleidung am Laptop, im Hintergrund eine Kollegin in der Werkstatt"></div>
  <div class="fade-left"></div>
  <div class="fade-bottom"></div>

  <div class="brand">
    <span class="brand-mark"></span>
    <span class="brand-name">wagenfeld</span>
  </div>

  <p class="eyebrow">AUSBILDUNG</p>

  <h1 class="headline">Lust auf<br>eine Ausbildung<br>bei uns?<span class="slash"></span></h1>

  <ul class="professions">
    <li>KFZ-Mechatroniker (m/w/d) /</li>
    <li>Automobilkaufmann (m/w/d) /</li>
    <li>Fachkraft für Lagerlogistik (m/w/d)</li>
  </ul>

  <a class="apply-button" href="#">JETZT BEWERBEN !</a>

  <div class="contact contact--web">
    <span class="contact-icon">
      <svg width="30" height="30" viewBox="0 0 30 30" fill="none" stroke="#fff" stroke-width="2">
        <circle cx="15" cy="15" r="12"/><ellipse cx="15" cy="15" rx="5.5" ry="12"/>
        <line x1="3" y1="15" x2="27" y2="15"/><line x1="5" y1="9" x2="25" y2="9"/><line x1="5" y1="21" x2="25" y2="21"/>
      </svg>
    </span>
    <span>www.kfzjobs.wagenfeld-auto.de</span>
  </div>

  <div class="contact contact--mail">
    <span class="contact-icon">
      <svg width="30" height="30" viewBox="0 0 30 30" fill="none" stroke="#fff" stroke-width="2">
        <rect x="5" y="8" width="20" height="14" rx="1.5"/><polyline points="5,9 15,16 25,9"/>
      </svg>
    </span>
    <span>jwagenfeld@wagenfeld-auto.de</span>
  </div>

  <svg class="chevrons" width="72" height="36" viewBox="0 0 72 36" fill="none" stroke="#f2ee1f" stroke-width="3">
    <polyline points="2,2 18,18 2,34"/><polyline points="26,2 42,18 26,34"/><polyline points="50,2 66,18 50,34"/>
  </svg>
</main>
</body>
</html>
```